wine label for ultra premium vineyard in Bendigo, Central Otago, New Zealand

"WREN" is our new wine brand, with grapes grown in our spectacular "ter Bosch" vineyard. The small, elevated vineyard overlooks a river valley and snowy mountains. We would like a highly elegant label for our 2018 pinot noir wine, which highlights the quality of wine and our very special vineyard location. "WREN" has to be prominent, with secondary emphasis on "ter Bosch vineyard" and "Bendigo, Central Otago". A stylized WREN logo (bird) could be a useful design device instead of the commonly seen illustrated mountain landscape (which is quite common for our local wines). Label size 90 high, 110 wide. Please use a pinot noir / burgundy bottle. See here for vineyard pics, and also below pics for other local wine labels and pics for inspiration / styles. https://www.instagram.com/jan.ter.bosch/

Target Market(s)

average bottle price for this premium red pinot noir would be aroundUS$40. target market are generally urban professionals aged 25 and older with a high degree of interest in pinot noir wine, and who are familiar with New Zealand pinot noir (ie. already know several brands).

Colors
ed252d

Requirements
Must have
• distinctive label, sophisticated look
Nice to have
• classy white paper stock
Should not have
• label must not get too busy... less but high quality and distinctive is more....

```html
<!DOCTYPE html>
<html lang="en">
<head>
<meta charset="utf-8">
<title>WREN Pinot Noir 2018 – Wine Label</title>
<link rel="stylesheet" href="https://fonts.googleapis.com/css2?family=IBM+Plex+Mono:wght@200&family=Outfit:wght@300&family=Permanent+Marker&family=Cormorant+Garamond:wght@500&display=swap">
<style>
  :root {
    --page: #171517;
    --paper: #e8e7e3;
    --wine: #780052;
    --wine-deep: #6d004a;
    --wine-bright: #880060;
    --ring: #dadada;
    --ring-hot: #d600b4;
    --ink-light: #f4eef2;
  }
  * { margin: 0; padding: 0; box-sizing: border-box; }
  html, body {
    width: 1200px;
    height: 1200px;
    overflow: hidden;
    background: var(--page);
  }
  .label {
    position: absolute;
    left: 40px;
    top: 139px;
    width: 1120px;
    height: 922px;
    background: var(--paper);
    color: var(--wine);
  }
  .label-graphics {
    position: absolute;
    inset: 0;
    width: 100%;
    height: 100%;
  }
  .brand-name {
    position: absolute;
    top: 78px;
    left: 0;
    width: 100%;
    text-align: center;
    font-family: "IBM Plex Mono", monospace;
    font-weight: 200;
    font-size: 104px;
    line-height: 1;
    letter-spacing: 6px;
    color: var(--wine);
  }
  .band-text {
    position: absolute;
    top: 441px;
    font-family: "Outfit", sans-serif;
    font-weight: 300;
    font-size: 43px;
    line-height: 1;
    color: var(--ink-light);
    transform: translateX(-50%);
    white-space: nowrap;
  }
  .vintage { left: 148px; }
  .varietal { left: 974px; }
  .vineyard-name {
    position: absolute;
    top: 745px;
    left: 0;
    width: 100%;
    text-align: center;
    font-family: "Permanent Marker", cursive;
    font-size: 42px;
    line-height: 1;
    letter-spacing: 1px;
    color: var(--wine);
  }
  .region {
    position: absolute;
    top: 846px;
    left: 0;
    width: 100%;
    text-align: center;
    font-family: "Cormorant Garamond", serif;
    font-weight: 500;
    font-size: 38px;
    line-height: 1;
    letter-spacing: 1px;
    color: var(--wine);
  }
</style>
</head>
<body>
  <main class="label">
    <svg class="label-graphics" viewBox="0 0 1120 922" xmlns="http://www.w3.org/2000/svg">
      <defs>
        <linearGradient id="band-fill" x1="0" x2="1" y1="0" y2="0">
          <stop offset="0" stop-color="var(--wine-deep)"/>
          <stop offset="1" stop-color="var(--wine-bright)"/>
        </linearGradient>
        <clipPath id="band-clip">
          <rect x="0" y="362" width="1120" height="198"/>
        </clipPath>
        <radialGradient id="bird-tone" cx="0.5" cy="0.45" r="0.6">
          <stop offset="0" stop-color="#c9a6bc"/>
          <stop offset="1" stop-color="#7a0052"/>
        </radialGradient>
      </defs>
      <rect class="band" x="0" y="362" width="1120" height="198" fill="url(#band-fill)"/>
      <circle class="emblem-ring" cx="557" cy="460" r="260" fill="var(--ring)"/>
      <circle class="emblem-ring-band" cx="557" cy="460" r="260" fill="var(--ring-hot)" clip-path="url(#band-clip)"/>
      <circle class="emblem-disc" cx="557" cy="460" r="237" fill="var(--wine)"/>
      <rect class="emblem-bird" x="423" y="344" width="242" height="248" rx="60" fill="url(#bird-tone)" opacity="0.55" role="img" aria-label="Engraved white line illustration of a wren perched on a branch"/>
    </svg>
    <h1 class="brand-name">WREN</h1>
    <p class="band-text vintage">2018</p>
    <p class="band-text varietal">PINOT NOIR</p>
    <p class="vineyard-name">TER BOSCH VINEYARD</p>
    <p class="region">BENDIGO, CENTRAL OTAGO, NZ</p>
  </main>
</body>
</html>
```